Business card design needed

We are 2 artists starting up a studio by the water in Sydney ...where we can work and display our art...would like the back ground to be Navy and white stripe...nautical...and the name The Paint Hut to be bold and the main wording...not nautical...if possible thought the A for art could be an easel ...ie the capital A using the cross bar as the platform that paint would be circles of colour....would like the main wording in Black but the easel A in colour
Hope u are able to help
thanku Lorna Vesk
as I will be away in a week for 4 weeks could u please send all info to Mira Colbins email....she can contact me and we can go ahead asap....

Artists

THE PAINT HUT

Hallorans Oar House
The Reach..17 Kellaby Rd..Dunrook 2091 Sydney

Mir Colbin..0437819025..miracolbin@mailnest.example
Lorn Vesk...0429573816..lvesk@harborlink.example

```html
<!DOCTYPE html>
<html lang="en">
<head>
<meta charset="utf-8">
<title>The Paint Hut – Business Card</title>
<link href="https://fonts.googleapis.com/css2?family=Cabin:wght@400;500&display=swap" rel="stylesheet">
<style>
  :root {
    --navy: #1e1b55;
    --sky: #1a9cd8;
    --sea: #069fdd;
    --ink: #0a0a0a;
    --paper: #ffffff;
  }
  html, body {
    margin: 0;
    padding: 0;
    width: 1200px;
    height: 1000px;
    overflow: hidden;
    background: var(--paper);
  }
  .canvas {
    position: relative;
    width: 1200px;
    height: 1000px;
  }
  .card {
    position: absolute;
    left: 0;
    top: 0;
    font-family: "Cabin", Arial, sans-serif;
  }
  .stripe { fill: var(--navy); }
  .sun { fill: var(--sky); }
  .sea { fill: var(--sea); }
  .brand-name {
    font-size: 64px;
    font-weight: 500;
    fill: var(--ink);
  }
  .address {
    font-size: 20px;
    fill: var(--navy);
  }
  .contact {
    font-size: 19px;
    fill: var(--paper);
  }
  .contact .person { font-size: 21px; }
</style>
</head>
<body>
<div class="canvas">
  <svg class="card" width="1200" height="1000" viewBox="0 0 1200 1000" xmlns="http://www.w3.org/2000/svg">
    <defs>
      <pattern id="navy-stripes" x="310" y="0" width="22.4" height="10" patternUnits="userSpaceOnUse">
        <rect class="stripe" x="0" y="0" width="12" height="10"/>
      </pattern>
      <clipPath id="card-edge">
        <rect x="302" y="221" width="632" height="354"/>
      </clipPath>
    </defs>

    <g clip-path="url(#card-edge)">
      <rect x="310" y="221" width="412" height="56" fill="url(#navy-stripes)"/>
      <rect x="310" y="397" width="618" height="82" fill="url(#navy-stripes)"/>

      <circle class="sun" cx="870" cy="260" r="153"/>

      <path class="sea" d="M302,470
        C330,480 355,470 372,447
        C392,484 449,484 469,447
        C489,484 546,484 566,447
        C586,484 643,484 663,447
        C683,484 740,484 760,447
        C780,484 837,484 857,447
        C877,484 914,482 934,470
        L934,575 L302,575 Z"/>
    </g>

    <text class="brand-name" x="333" y="369">The Paint Hut</text>

    <text class="address" text-anchor="end">
      <tspan x="915" y="255">THE PAINT HUT</tspan>
      <tspan x="915" y="281">Hallorans Oar House</tspan>
      <tspan x="915" y="307">The Reach</tspan>
      <tspan x="915" y="333">17 Kellaby Rd</tspan>
      <tspan x="915" y="359">Dunrook 2091</tspan>
      <tspan x="915" y="385">Sydney</tspan>
    </text>

    <text class="contact">
      <tspan class="person" x="336" y="502">Lorn Vesk</tspan>
      <tspan x="336" y="528">0429573816</tspan>
      <tspan x="336" y="554">lvesk@harborlink.example</tspan>
    </text>
    <text class="contact">
      <tspan class="person" x="584" y="502">Mir Colbin</tspan>
      <tspan x="584" y="528">0437819025</tspan>
      <tspan x="584" y="554">miracolbin@mailnest.example</tspan>
    </text>
  </svg>
</div>
</body>
</html>
```